Modern Website Design for PollMeridian – CX & Loyalty SaaS Platform

We need a modern, professional, and responsive website design for our B2B SaaS platform, PollMeridian. We help companies collect real-time customer feedback, analyze insights, and improve loyalty — combining a powerful CX platform with expert consulting services. The website should clearly communicate who we are and what we offer within the first impression. It should balance data-driven visuals such as dashboards, analytics, and charts with a human, approachable feel. The design must include at least six key pages: Homepage, Product/Services, About, Blog/Resources, Contact/Demo, and Pricing. It should be conversion-focused with clear calls-to-action that encourage visitors to request a demo or contact us. The site must be fully responsive across desktop, tablet, and mobile. It should support multiple languages, starting with English and Danish. Most importantly, the delivery must be a final WordPress website, ready to go live, not just design files.

Target Market(s)

Our target market is medium-to-large B2B organizations. The primary audience includes CX leaders, executives, and managers in customer success and service who want to measure loyalty, understand customer insights, and improve retention.

Industry/Entity Type

Technology / SaaS / Customer Experience

Coding

Coded - Design and coding required

Number of Pages Required

5+ page

Font styles to use
Sans Serif

Requirements
Must have
• The project must deliver a final WordPress website that is fully responsive across all devices. The design should be clean, modern, and SaaS-inspired, with clear calls-to-action on every page. It must also support English and Danish, with a visible language toggle. The site should include visuals of dashboards and analytics that reflect data-driven insights. It must feature sections for case studies or testimonials to build trust. The copywriting should be SEO-friendly, and the design should include smooth animations or hover effects that add polish without making the website feel heavy.
Should not have
• Cluttered layouts, or generic stock photos such as handshakes

```html
<!DOCTYPE html>
<html lang="en">
<head>
<meta charset="utf-8">
<title>PollMeridian – Website Pages</title>
<link href="https://fonts.googleapis.com/css2?family=Rajdhani:wght@400;500;600;700&display=swap" rel="stylesheet">
<style>
:root{
  --stage:#999999;
  --bg:#0c1328;
  --bg-2:#111a38;
  --header:#070b17;
  --card:#0f1834;
  --card-line:#1f2b4f;
  --text:#ffffff;
  --muted:#9aa4c0;
  --accent:#ff4718;
  --navy:#1d3a8f;
  --mock:#1b2254;
  --green:#1fb866;
  --row:#141e3d;
}
*{box-sizing:border-box;margin:0;padding:0}
html,body{width:1200px;height:585px;overflow:hidden;background:var(--stage)}
body{font-family:"Rajdhani",sans-serif;color:var(--text)}
.board{position:absolute;left:0;top:0;width:2576px;height:1256px;transform:scale(.46584);transform-origin:0 0}
.page{position:absolute;width:785px;background:linear-gradient(160deg,var(--bg) 0%,var(--bg-2) 100%);overflow:hidden;box-shadow:0 2px 10px rgba(0,0,0,.25)}
.page *{position:absolute}
.page .inline,.page .inline *{position:static}
.header{left:0;top:0;width:785px;height:40px;background:var(--header);border-bottom:1px solid #151d36}
.brand{left:148px;top:10px;height:20px;display:flex;align-items:center;gap:6px;font-weight:700;font-size:15px;letter-spacing:.3px}
.brand .inline.dot{width:14px;height:14px;border-radius:50%;background:var(--accent);display:inline-block}
.nav{left:442px;top:15px;display:flex;gap:9px;font-size:6.5px;font-weight:600}
.nav span{position:static}
.btn{display:flex;align-items:center;justify-content:center;border-radius:12px;font-weight:700;font-size:6.5px;color:#fff}
.btn-accent{background:var(--accent)}
.btn-navy{background:var(--navy)}
.btn-ghost{border:1px solid var(--card-line);background:#0a1124}
.header .btn{left:585px;top:10px;width:55px;height:20px}
.lang{top:12px;width:14px;height:11px;border-radius:6px;font-size:5px;font-weight:700;display:flex;align-items:center;justify-content:center;background:#1a2240;color:#ccd}
.lang.on{left:743px;background:var(--green);color:#fff}
.lang.off{left:761px}
.eyebrow{font-size:4.8px;font-weight:700;letter-spacing:1.3px;color:#cfd5e6;text-transform:uppercase}
.title{font-weight:700;font-size:21px;line-height:1.15}
.title .hl{color:var(--accent)}
.h2{font-weight:700;font-size:13px}
.copy{font-size:6.3px;line-height:1.4;color:var(--muted)}
.card{background:var(--card);border:1px solid var(--card-line);border-radius:6px}
.card .ct{left:8px;top:8px;font-size:6.8px;font-weight:700}
.card .cp{left:8px;top:20px;right:8px;font-size:5.3px;line-height:1.4;color:var(--muted)}
.chip{font-size:4.3px;border:1px solid var(--card-line);border-radius:6px;padding:2px 5px;color:#c6cde0;background:#0c1430}
.center{left:0;width:785px;text-align:center}
.footer{left:0;width:785px;border-top:1px solid #1a2443;height:90px}
.footer .fbrand{left:147px;top:14px;font-weight:700;font-size:8.5px}
.footer .ftag{left:147px;top:30px;font-size:5.2px;color:var(--muted)}
.footer .chip{left:147px;top:42px}
.footer .fcol{top:14px;font-size:5.3px;line-height:2.1;color:var(--muted)}
.footer .fcol b{display:block;font-size:4.5px;letter-spacing:1.2px;color:#cfd5e6}
.icon{width:22px;height:22px;border:1px solid #2c3758;border-radius:4px;background:#0d1530}
.mock{left:147px;top:421px;width:491px;height:286px;background:var(--mock);border-radius:4px;display:flex;align-items:center;justify-content:center;font-size:27px;font-weight:700;letter-spacing:2px;color:#b8bccd}
.table-head{left:147px;top:114px;width:491px;height:18px;background:var(--row);border-radius:3px}
.cell{font-size:5.5px;color:#c6cde0}
.cell.b{font-weight:700;color:#fff}
.rule{left:147px;width:491px;height:1px;background:var(--green)}
.field{left:8px;width:225px;height:15px;border:1px solid var(--card-line);border-radius:3px;background:#0a1229}
.label{left:8px;font-size:5.3px;font-weight:700}
.faq p{position:static;font-size:5.2px;color:var(--muted);line-height:1.3}
.faq b{font-size:5.2px;color:#fff;display:block}
.glow{left:-60px;top:0;width:220px;height:200px;background:radial-gradient(circle at 40% 40%,rgba(190,50,30,.55),rgba(190,50,30,0) 65%)}
</style>
</head>
<body>
<div class="board">

<!-- Homepage -->
<section class="page" style="left:61px;top:61px;height:1133px">
  <div class="glow"></div>
  <header class="header">
    <div class="brand"><span class="inline dot"></span><span class="inline">PollMeridian</span></div>
    <nav class="nav"><span>Home</span><span>Product</span><span>About</span><span>Resources</span><span>Pricing</span></nav>
    <div class="btn btn-accent">Request Demo</div>
    <div class="lang on">EN</div><div class="lang off">DA</div>
  </header>
  <div class="eyebrow" style="left:147px;top:117px">Customer experience platform</div>
  <h1 class="title" style="left:147px;top:127px;width:260px">Real-time insights. <span class="inline hl">Loyal customers.</span></h1>
  <p class="copy" style="left:147px;top:178px;width:240px">Collect feedback across journeys, surface churn risks instantly, and act with guidance from CX experts.</p>
  <div class="btn btn-accent" style="left:147px;top:208px;width:71px;height:19px">Request a Demo</div>
  <div class="btn btn-ghost" style="left:224px;top:208px;width:84px;height:19px">Explore the Platform</div>
  <div class="chip" style="left:147px;top:236px">Leadership-ready reports</div>
  <div class="chip" style="left:212px;top:236px">Churn risk alerts</div>
  <div class="chip" style="left:258px;top:236px">Consulting included</div>

  <div class="card" style="left:420px;top:105px;width:220px;height:156px">
    <div class="h2" style="left:20px;top:15px;font-size:11.5px">WHAT YOU GET</div>
    <div class="icon" style="left:20px;top:42px"></div>
    <div class="ct" style="left:51px;top:43px">Analyze in minutes</div>
    <div class="cp" style="left:51px;top:54px">Dashboards, trends, and segments give instant clarity.</div>
    <div class="icon" style="left:20px;top:77px"></div>
    <div class="ct" style="left:51px;top:78px">Act faster</div>
    <div class="cp" style="left:51px;top:89px">Real-time alerts and workflows to reduce churn.</div>
    <div class="icon" style="left:20px;top:112px"></div>
    <div class="ct" style="left:51px;top:113px">Expert help</div>
    <div class="cp" style="left:51px;top:124px">Our consultants guide setup, interpretation, and action.</div>
  </div>

  <div class="eyebrow center" style="top:372px">Showcase</div>
  <h2 class="h2 center" style="top:380px">Leadership-ready dashboards</h2>
  <p class="copy center" style="top:400px">Replace these with real screenshots. The layout is ready for high-credibility product visuals.</p>
  <div class="mock" role="img" aria-label="Analytics dashboard preview placeholder">DASHBOARD MOCKUP</div>

  <div class="card" style="left:147px;top:800px;width:158px;height:49px"><div class="ct">Collect</div><div class="cp">Multi-channel surveys capture real-time signals across journeys.</div></div>
  <div class="card" style="left:313px;top:800px;width:158px;height:49px"><div class="ct">Analyze</div><div class="cp">Segment by account, touchpoint, owner; filter by sentiment and themes.</div></div>
  <div class="card" style="left:479px;top:800px;width:159px;height:49px"><div class="ct">Improve</div><div class="cp">Close the loop with alerts, playbooks, and expert guidance.</div></div>

  <h2 class="h2 center" style="top:938px">Ready to see PollMeridian in action?</h2>
  <p class="copy center" style="top:958px">Book a live walkthrough tailored to your customer journey.</p>
  <div class="btn btn-navy" style="left:365px;top:973px;width:55px;height:20px">Request Demo</div>

  <footer class="footer" style="top:1044px">
    <div class="fbrand">PollMeridian</div>
    <div class="ftag">Real-time CX insights. Expert consulting.</div>
    <div class="chip">© 2025 PollMeridian</div>
    <div class="fcol" style="left:392px"><b>COMPANY</b>About<br>Resources<br>Pricing</div>
    <div class="fcol" style="left:519px"><b>CONNECT</b>Contact<br>hello@pollmeridian.com</div>
  </footer>
</section>

<!-- Product -->
<section class="page" style="left:897px;top:61px;height:457px">
  <header class="header">
    <div class="brand"><span class="inline dot"></span><span class="inline">PollMeridian</span></div>
    <nav class="nav"><span>Home</span><span>Product</span><span>About</span><span>Resources</span><span>Pricing</span></nav>
    <div class="btn btn-accent">Request Demo</div>
    <div class="lang on">EN</div><div class="lang off">DA</div>
  </header>
  <div class="eyebrow" style="left:147px;top:80px">Platform</div>
  <h1 class="title" style="left:147px;top:86px">All-in-one CX + Loyalty</h1>
  <div class="card" style="left:147px;top:112px;width:158px;height:50px"><div class="ct">Real-time Feedback</div><div class="cp">Collect NPS, CSAT, and custom surveys across email, web, and in-app.</div></div>
  <div class="card" style="left:313px;top:112px;width:158px;height:50px"><div class="ct">Segmentation &amp; Themes</div><div class="cp">Slice by account, product, region. Auto-tag comments with themes.</div></div>
  <div class="card" style="left:479px;top:112px;width:159px;height:50px"><div class="ct">Leadership Reporting</div><div class="cp">Share concise scorecards with trends, drivers, and benchmarks.</div></div>

  <div class="eyebrow" style="left:147px;top:241px">Consulting</div>
  <h2 class="h2" style="left:147px;top:246px">Expert support included</h2>
  <p class="copy" style="left:147px;top:265px">We don't just show dashboards—we help you design programs and act on insights.</p>
  <div class="card" style="left:147px;top:279px;width:158px;height:50px"><div class="ct">Program Design</div><div class="cp">Journeys, metrics, sampling, and governance.</div></div>
  <div class="card" style="left:313px;top:279px;width:158px;height:50px"><div class="ct">Enablement</div><div class="cp">Playbooks for closing the loop and driving adoption.</div></div>
  <div class="card" style="left:479px;top:279px;width:159px;height:50px"><div class="ct">Executive Alignment</div><div class="cp">Monthly reviews and quarterly planning with your leaders.</div></div>
  <div class="btn btn-accent" style="left:359px;top:329px;width:67px;height:20px">Talk to a CX expert</div>

  <footer class="footer" style="top:389px">
    <div class="fbrand">PollMeridian</div>
    <div class="ftag">Real-time CX insights. Expert consulting.</div>
    <div class="chip">© 2025 PollMeridian</div>
    <div class="fcol" style="left:392px"><b>COMPANY</b>About<br>Resources<br>Pricing</div>
    <div class="fcol" style="left:519px"><b>CONNECT</b>Contact<br>hello@pollmeridian.com</div>
  </footer>
</section>

<!-- About -->
<section class="page" style="left:897px;top:564px;height:281px">
  <header class="header">
    <div class="brand"><span class="inline dot"></span><span class="inline">PollMeridian</span></div>
    <nav class="nav"><span>Home</span><span>Product</span><span>About</span><span>Resources</span><span>Pricing</span></nav>
    <div class="btn btn-accent">Request Demo</div>
    <div class="lang on">EN</div><div class="lang off">DA</div>
  </header>
  <div class="eyebrow" style="left:147px;top:80px">About</div>
  <h1 class="title" style="left:147px;top:86px">Why PollMeridian?</h1>
  <p class="copy" style="left:147px;top:113px;width:220px">We combine a powerful CX platform with hands-on experts who help you interpret and act.</p>
  <p class="copy" style="left:157px;top:138px;color:#d4d9e8;line-height:1.45">• <b class="inline">Trust:</b> Enterprise-ready security &amp; privacy.<br>• <b class="inline">Impact:</b> Programs designed for measurable results.<br>• <b class="inline">Partnership:</b> We're an extension of your team.</p>
  <div class="card" style="left:396px;top:78px;width:242px;height:92px">
    <div class="h2" style="left:8px;top:8px;font-size:11.5px">Our mission</div>
    <div class="cp" style="top:28px">Help companies earn loyalty by understanding customers and closing experience gaps—fast.</div>
    <div class="chip" style="left:8px;top:46px">Copenhagen · Global remote</div>
  </div>
  <footer class="footer" style="top:210px">
    <div class="fbrand">PollMeridian</div>
    <div class="ftag">Real-time CX insights. Expert consulting.</div>
    <div class="chip">© 2025 PollMeridian</div>
    <div class="fcol" style="left:392px"><b>COMPANY</b>About<br>Resources<br>Pricing</div>
    <div class="fcol" style="left:519px"><b>CONNECT</b>Contact<br>hello@pollmeridian.com</div>
  </footer>
</section>

<!-- Resources -->
<section class="page" style="left:897px;top:890px;height:304px">
  <header class="header">
    <div class="brand"><span class="inline dot"></span><span class="inline">PollMeridian</span></div>
    <nav class="nav"><span>Home</span><span>Product</span><span>About</span><span>Resources</span><span>Pricing</span></nav>
    <div class="btn btn-accent">Request Demo</div>
    <div class="lang on">EN</div><div class="lang off">DA</div>
  </header>
  <div class="eyebrow" style="left:147px;top:79px">Resources</div>
  <h1 class="title" style="left:147px;top:85px">Insights &amp; case studies</h1>
  <div class="card" style="left:147px;top:114px;width:158px;height:79px"><div class="ct">Designing a modern NPS program</div><div class="cp">Guide · 6 min<br>Sampling, multi-journey design, and how to drive adoption.</div><div class="btn btn-ghost" style="left:8px;top:53px;width:30px;height:14px">Read</div></div>
  <div class="card" style="left:313px;top:114px;width:158px;height:79px"><div class="ct">Reducing churn with real-time alerts</div><div class="cp">Case study · 4 min<br>How a B2B SaaS cut churn 18% by closing the loop faster.</div><div class="btn btn-ghost" style="left:8px;top:53px;width:30px;height:14px">Read</div></div>
  <div class="card" style="left:479px;top:114px;width:159px;height:79px"><div class="ct">Executive reporting that drives change</div><div class="cp">Playbook · 5 min<br>What leaders actually want to see—and what to remove.</div><div class="btn btn-ghost" style="left:8px;top:53px;width:30px;height:14px">Read</div></div>
  <footer class="footer" style="top:233px">
    <div class="fbrand">PollMeridian</div>
    <div class="ftag">Real-time CX insights. Expert consulting.</div>
    <div class="chip">© 2025 PollMeridian</div>
    <div class="fcol" style="left:392px"><b>COMPANY</b>About<br>Resources<br>Pricing</div>
    <div class="fcol" style="left:519px"><b>CONNECT</b>Contact<br>hello@pollmeridian.com</div>
  </footer>
</section>

<!-- Pricing -->
<section class="page" style="left:1729px;top:61px;height:344px">
  <header class="header">
    <div class="brand"><span class="inline dot"></span><span class="inline">PollMeridian</span></div>
    <nav class="nav"><span>Home</span><span>Product</span><span>About</span><span>Resources</span><span>Pricing</span></nav>
    <div class="btn btn-accent">Request Demo</div>
    <div class="lang on">EN</div><div class="lang off">DA</div>
  </header>
  <div class="eyebrow" style="left:147px;top:80px">Pricing</div>
  <h1 class="title" style="left:147px;top:86px">Choose the plan that fits</h1>
  <div class="table-head"></div>
  <div class="cell b" style="left:154px;top:120px">Plan</div>
  <div class="cell b" style="left:231px;top:120px">Best for</div>
  <div class="cell b" style="left:336px;top:120px">Highlights</div>

  <div class="cell b" style="left:154px;top:147px">Starter</div>
  <div class="cell" style="left:231px;top:147px">Small teams, one journey</div>
  <div class="cell" style="left:336px;top:147px">NPS/CSAT, dashboards, email capture, basic alerts</div>
  <div class="cell b" style="left:563px;top:147px">Request demo</div>

  <div class="rule" style="top:167px"></div>
  <div class="cell b" style="left:154px;top:180px">Pro</div>
  <div class="chip" style="left:168px;top:179px">Most popular</div>
  <div class="cell" style="left:231px;top:180px">Growing CX programs</div>
  <div class="cell" style="left:336px;top:180px">Multi-journey, segments &amp; themes, integrations, playbooks</div>
  <div class="btn btn-accent" style="left:556px;top:174px;width:30px;height:19px">Start</div>
  <div class="rule" style="top:201px"></div>

  <div class="cell b" style="left:154px;top:213px">Enterprise</div>
  <div class="cell" style="left:231px;top:213px">Global programs</div>
  <div class="cell" style="left:336px;top:213px">Advanced governance, SSO, custom SLAs, dedicated expert</div>
  <div class="cell b" style="left:564px;top:213px">Talk to sales</div>

  <footer class="footer" style="top:272px">
    <div class="fbrand">PollMeridian</div>
    <div class="ftag">Real-time CX insights. Expert consulting.</div>
    <div class="chip">© 2025 PollMeridian</div>
    <div class="fcol" style="left:392px"><b>COMPANY</b>About<br>Resources<br>Pricing</div>
    <div class="fcol" style="left:519px"><b>CONNECT</b>Contact<br>hello@pollmeridian.com</div>
  </footer>
</section>

<!-- Contact -->
<section class="page" style="left:1729px;top:451px;height:483px">
  <header class="header">
    <div class="brand"><span class="inline dot"></span><span class="inline">PollMeridian</span></div>
    <nav class="nav"><span>Home</span><span>Product</span><span>About</span><span>Resources</span><span>Pricing</span></nav>
    <div class="btn btn-accent">Request Demo</div>
    <div class="lang on">EN</div><div class="lang off">DA</div>
  </header>
  <div class="eyebrow" style="left:147px;top:78px">Contact</div>
  <h1 class="title" style="left:147px;top:84px;width:200px">Let's build loyalty together</h1>
  <p class="copy" style="left:147px;top:137px">Fill out the form and we'll respond within one business day.</p>
  <div class="card" style="left:147px;top:150px;width:241px;height:208px">
    <div class="label" style="top:14px">Name</div><div class="field" style="top:24px"></div>
    <div class="label" style="top:48px">Email</div><div class="field" style="top:58px"></div>
    <div class="label" style="top:83px">Company</div><div class="field" style="top:93px"></div>
    <div class="label" style="top:117px">Message</div><div class="field" style="top:127px;height:50px"></div>
    <div class="btn btn-navy" style="left:8px;top:181px;width:55px;height:18px">Request Demo</div>
  </div>
  <p class="copy" style="left:147px;top:361px;color:#d4d9e8">Or email us: <span class="inline" style="color:#3b5bd6;text-decoration:underline">hello@pollmeridian.com</span></p>
  <div class="card faq" style="left:397px;top:79px;width:241px;height:294px">
    <div class="h2" style="left:9px;top:8px;font-size:11.5px">FAQ</div>
    <div style="left:9px;top:28px;right:9px">
      <b class="inline">Is it multilingual?</b><p>Yes—English and Danish are supported with a header toggle.</p>
      <b class="inline" style="margin-top:3px">Do you help with rollout?</b><p>Yes—our consultants guide implementation and adoption.</p>
      <b class="inline" style="margin-top:3px">Can you integrate with our stack?</b><p>We support common CRMs, BI tools, and data pipelines.</p>
    </div>
  </div>
  <footer class="footer" style="top:413px">
    <div class="fbrand">PollMeridian</div>
    <div class="ftag">Real-time CX insights. Expert consulting.</div>
    <div class="chip">© 2025 PollMeridian</div>
    <div class="fcol" style="left:392px"><b>COMPANY</b>About<br>Resources<br>Pricing</div>
    <div class="fcol" style="left:519px"><b>CONNECT</b>Contact<br>hello@pollmeridian.com</div>
  </footer>
</section>

</div>
</body>
</html>
```